Rivolex.com Trucking Company Website

Need a website designed (no content) for a trucking company, specializing in trucking of ocean containers (intermodal Trucking). Heavy emphasis on technology, using latest technology, providing unabated visibility and realtime information.
clean minimalist industrial website
example:
https://www.bramtiq.com/

Target Market(s)

Professional Business Consumer corporate and small business

Industry/Entity Type

Trucking Company

Number of Pages Required

5+ page

Requirements
Must have
• Industrial Design, simple informative, for a busy professional to view and get the necessary information with out the distractions.
• Blog Page
• Client Log-In on the front page
• Technology page - showing our intensive investments in technology
Nice to have
• If ANY images included, MUST be USA related. Example if include an image of a truck, ensure its a USA model. Do the research.
• included our business card for sample of Logo
• Doesnt not have to be the same color schemes.
Should not have
• moving images

```html
<!DOCTYPE html>
<html lang="en">
<head>
<meta charset="utf-8">
<title>Rivolex Consulting</title>
<link href="https://fonts.googleapis.com/css2?family=Exo+2:wght@600;700;800&family=Lato:wght@400;700&display=swap" rel="stylesheet">
<style>
:root{
  --blue:#15589a;
  --blue-dark:#0f4a85;
  --ink:#2b2b2b;
  --white:#ffffff;
  --card:#f8f8f8;
  --line:#d8d8d8;
  --black:#050505;
  --text:#444;
}
*{margin:0;padding:0;box-sizing:border-box}
html,body{width:1200px;height:1040px;overflow:hidden;background:var(--white);font-family:'Lato',sans-serif}
.page{position:relative;width:1200px;height:1040px}
.hero{position:absolute;left:0;top:0;width:1200px;height:626px;border-top:3px solid var(--blue);
  background:
   radial-gradient(ellipse 300px 260px at 550px 330px, rgba(216,178,150,.55), rgba(216,178,150,0) 70%),
   linear-gradient(90deg,#1a1d22 0%,#262a30 22%,#6f7f93 42%,#98a9bf 62%,#8ea1ba 85%,#7d91ad 100%);}
.hero::after{content:"";position:absolute;inset:0;background:linear-gradient(180deg,rgba(10,15,25,.55) 0%,rgba(10,15,25,0) 18%,rgba(10,15,25,0) 70%,rgba(20,30,50,.3) 100%)}
.logo{position:absolute;left:99px;top:22px;z-index:2;color:var(--white);font-family:'Exo 2',sans-serif}
.logo .name{display:block;font-weight:800;font-size:44px;letter-spacing:2px;line-height:46px}
.logo .sub{display:block;font-weight:800;font-size:15px;letter-spacing:9.3px;line-height:18px}
.nav{position:absolute;top:30px;right:99px;z-index:2;display:flex;align-items:center;height:42px}
.nav a{color:var(--white);text-decoration:none;font-size:15px;letter-spacing:.3px;font-family:'Lato',sans-serif}
.nav .sep{width:1px;height:16px;background:rgba(255,255,255,.3);margin:0 33px}
.nav .sep.tall{height:40px;margin:0 32px 0 36px;background:rgba(255,255,255,.4)}
.login{display:flex;align-items:center;gap:7px;height:42px;padding:0 17px;background:var(--blue);border:1px solid #5ea0e0}
.headline{position:absolute;top:484px;left:0;width:1200px;text-align:center;z-index:2;color:var(--white);
  font-family:'Exo 2',sans-serif;font-weight:700;font-size:46px;letter-spacing:.5px;text-shadow:0 3px 8px rgba(0,0,0,.45)}
.services{position:absolute;left:99px;top:575px;width:1002px;height:340px;background:var(--white);border-radius:3px 3px 0 0;box-shadow:0 -2px 14px rgba(0,0,0,.12)}
.card{position:absolute;top:28px;width:300px;height:278px;background:var(--card);border:1px solid var(--line);border-radius:2px;text-align:center;box-shadow:0 10px 10px -8px rgba(0,0,0,.25)}
.card h2{font-family:'Exo 2',sans-serif;font-weight:700;font-size:23px;color:var(--ink);margin-top:22px;line-height:28px}
.card p{font-size:12.5px;line-height:19.5px;color:var(--text);margin:0 auto;width:240px}
.badge{width:122px;height:122px;margin:16px auto 19px;border-radius:50%;background:var(--blue);border:3px solid var(--blue);box-shadow:inset 0 0 0 3px var(--white);display:flex;align-items:center;justify-content:center}
.card.active{background:var(--blue);border:8px solid var(--blue);padding:0}
.card.active .inner{position:absolute;inset:0;border:2px solid #d7e6f7;border-radius:2px;
  background:linear-gradient(180deg,#2f6fb0 0%,#2a6aa8 55%,#2d6aa0 75%,#1c5690 100%)}
.card.active h2{position:relative;color:var(--white);margin-top:14px}
.card.active .badge{position:relative;margin-top:16px;border-color:#cfd8e2;box-shadow:inset 0 0 0 3px var(--white),0 0 0 2px #9fb4ca}
.card.active p{position:relative;color:#e8f0f9}
.c1{left:25px}.c2{left:351px}.c3{left:678px}
.contact{position:absolute;left:0;top:942px;width:1200px;height:56px;background:var(--black);display:flex;align-items:center;justify-content:center;gap:36px;color:var(--white);font-size:15.5px}
.contact span{display:flex;align-items:center;gap:9px}
.bottom{position:absolute;left:0;top:998px;width:1200px;height:42px;background:var(--blue);color:var(--white)}
.bottom .copy{position:absolute;left:99px;top:12px;font-weight:700;font-size:14px}
.social{position:absolute;right:84px;top:6px;display:flex;gap:6px}
.social i{display:block;width:29px;height:29px;border-radius:50%;background:var(--white)}
</style>
</head>
<body>
<div class="page">
  <header class="hero" role="img" aria-label="Businessman in a dark suit touching a glowing world map network of connected points">
    <div class="logo"><span class="name">RIVOLEX</span><span class="sub">CONSULTING</span></div>
    <nav class="nav">
      <a href="#">BLOG</a><span class="sep"></span>
      <a href="#">TECHNOLOGY</a><span class="sep tall"></span>
      <a class="login" href="#">
        <svg width="17" height="15" viewBox="0 0 17 15"><path d="M9 1h6a1 1 0 0 1 1 1v11a1 1 0 0 1-1 1H9" fill="none" stroke="#fff" stroke-width="2"/><path d="M1 5.5h5V2l5.5 5.5L6 13V9.5H1z" fill="#fff"/></svg>
        CLIENT LOGIN</a>
    </nav>
    <h1 class="headline">TECHNOLOGY DRIVEN COMPANY</h1>
  </header>

  <section class="services">
    <article class="card c1">
      <h2>INTERMODAL TRUCKING</h2>
      <div class="badge">
        <svg width="58" height="72" viewBox="0 0 58 72" fill="#fff"><rect x="14" y="0" width="30" height="8" rx="1"/><rect x="10" y="10" width="38" height="26" rx="3"/><rect x="15" y="15" width="28" height="14" fill="#15589a"/><rect x="2" y="14" width="6" height="10"/><rect x="50" y="14" width="6" height="10"/><rect x="8" y="38" width="42" height="22" rx="2"/><rect x="18" y="42" width="22" height="12" fill="#15589a"/><rect x="4" y="56" width="50" height="5"/><rect x="10" y="62" width="8" height="9"/><rect x="40" y="62" width="8" height="9"/></svg>
      </div>
      <p>Lorem ipsum dolor sit amet, consectetuer adipiscing elit,sed consectetuer adipiscing elit,sed diam nonummy.</p>
    </article>
    <article class="card c2 active">
      <div class="inner" role="img" aria-label="Row of parked freight trucks in blue tint"></div>
      <h2>LTL</h2>
      <div class="badge">
        <svg width="62" height="40" viewBox="0 0 62 40"><rect x="0" y="0" width="42" height="30" rx="3" fill="#fff"/><path d="M44 8h9l8 10v12H44z" fill="#fff"/><circle cx="12" cy="32" r="7" fill="#fff" stroke="#15589a" stroke-width="2.5"/><circle cx="50" cy="32" r="7" fill="#fff" stroke="#15589a" stroke-width="2.5"/><text x="21" y="21" text-anchor="middle" font-family="Exo 2,sans-serif" font-weight="800" font-size="16" fill="#15589a">LTL</text></svg>
      </div>
      <p>Lorem ipsum dolor sit amet, consectetuer adipiscing elit,sed consectetuer adipiscing elit,sed diam nonummy.</p>
    </article>
    <article class="card c3">
      <h2>WAREHOUSING</h2>
      <div class="badge">
        <svg width="62" height="52" viewBox="0 0 62 52" fill="#fff"><path d="M31 0L62 12v40H0V12z"/><rect x="9" y="18" width="44" height="34" fill="#15589a"/><rect x="12" y="20" width="38" height="3"/><rect x="12" y="25" width="38" height="3"/><rect x="15" y="32" width="13" height="9"/><rect x="34" y="32" width="13" height="9"/><rect x="15" y="42" width="13" height="10"/><rect x="30" y="42" width="17" height="10"/></svg>
      </div>
      <p>Lorem ipsum dolor sit amet, consectetuer adipiscing elit,sed consectetuer adipiscing elit,sed diam nonummy.</p>
    </article>
  </section>

  <footer>
    <div class="contact">
      <span><svg width="17" height="24" viewBox="0 0 17 24"><path d="M8.5 0A8.5 8.5 0 0 0 0 8.5C0 15 8.5 24 8.5 24S17 15 17 8.5A8.5 8.5 0 0 0 8.5 0zm0 12a3.5 3.5 0 1 1 0-7 3.5 3.5 0 0 1 0 7z" fill="#fff"/></svg>2400 Harbor Lane Unit 4 Carteret, NJ 07008</span>
      <span><svg width="19" height="19" viewBox="0 0 24 24"><path d="M6.6 10.8a15.1 15.1 0 0 0 6.6 6.6l2.2-2.2a1 1 0 0 1 1-.25 11.4 11.4 0 0 0 3.6.57 1 1 0 0 1 1 1V20a1 1 0 0 1-1 1A17 17 0 0 1 3 4a1 1 0 0 1 1-1h3.5a1 1 0 0 1 1 1c0 1.25.2 2.45.57 3.57a1 1 0 0 1-.25 1z" fill="#fff"/></svg>908.555.0142</span>
      <span><svg width="21" height="15" viewBox="0 0 21 15"><rect width="21" height="15" rx="1" fill="#fff"/><path d="M1 1l9.5 7L20 1" fill="none" stroke="#050505" stroke-width="1.6"/></svg>contact@rivolex.com</span>
      <span><svg width="19" height="19" viewBox="0 0 20 20"><circle cx="10" cy="10" r="9.5" fill="#fff"/><path d="M5 5c2 0 3 1 2.5 3S9 10 8 12s1 4 1 5M12 3c0 2 2 2 3 3s-1 3 1 4" fill="none" stroke="#050505" stroke-width="1.8"/></svg>www.rivolex.com</span>
    </div>
    <div class="bottom">
      <p class="copy">Copyright 2017 info@rivolex.com. All rights reserved.</p>
      <div class="social" aria-label="Social links"><i></i><i></i><i></i><i></i></div>
    </div>
  </footer>
</div>
</body>
</html>
```